Create Website for new company called "Verdant Lodge 17"

Verdant Lodge 17 is a new business situated in Southwestern Colorado. We are creating a business that will rent out spaces where clients can grow their own marijuana. Picture a large green house with partitioned spaces that are secured by a lock. Best way to envision this would be to think of a storage business that rents out storage rooms. The difference is that we will be having the units inside a green house ( for growing purposes) Picture a small area that is secured by locks, Picture an area that has the ability to provide state of the art security, cameras etc. We want to focus our efforts on professionals, blue collar workers and end users of marijuana. Our emphasis is in the area of assisting those whom wish to grow their own plants. We want to provide them a safe facility in which to do that. . Keep in mind that we also build custom grow rooms at clients homes and provide a grow pod (lease these) where a small grow unit will be delivered and picked up from our clients whom want to lease a unit for a short amount of time. We have a business card ( just designed) and will send that information to those whom express an interests in this project. We want to be able to sign people up for our services by entering an agreement and signing the agreement while on the internet. We want to provide our services to those whom consume recreational and medical marijuana. This site will need to gather information I.e email addresses so that we can followup with offers. This is a tremendous opportunity for the right designer. We will be creating many more websites as other states come on line and make marijuana legal to consume. Use the business card model for a point of reference of how we envision the concept. That is a business card we just recently printed. The hands and the plant is our logo so far. Open to suggestions. There will be three levels of service. Bronze, Silver, Gold or Platinum. We will also have a retail biz down the road but not at the present time.

Target Market(s)

Ages 21-60

Industry/Entity Type

Medical

Logo Text

Verdant Lodge 17.

Number of Pages Required

5+ page

Requirements
Must have
• Clean appearance not to busy , easily navigable from link to link, page to page. Must have ability down the road to enter into a contractual agreement via the website. Must use our provided logo and example of that is on our business card that will be uploaded here shortly. We would like to have the colors that are on the business card however if you have suggestions or color schemes that you want us to consider that is okay.
Nice to have
• Nice to have a animation of seed to weed and how clients can save a tremendous amount of money growing their own cannabis. Nice to have testimonial page or feedback page. Have a membership component to website,
Should not have
• No flashing lights, etc. Not to busy in terms of animations.

```html
<!DOCTYPE html>
<html lang="en">
<head>
<meta charset="utf-8">
<title>Verdant Lodge 17</title>
<link href="https://fonts.googleapis.com/css2?family=Oswald:wght@400;500&family=PT+Serif&display=swap" rel="stylesheet">
<style>
:root{
  --green:#027a36;
  --green-dark:#01652c;
  --green-light:#1f9a4f;
  --orange:#dd7b34;
  --charcoal:#2f3436;
  --panel:#e9e9e9;
  --text:#555;
  --white:#fff;
}
*{margin:0;padding:0;box-sizing:border-box}
html,body{width:937px;height:1200px;overflow:hidden;background:var(--white)}
body{position:relative;font-family:Arial,Helvetica,sans-serif;color:var(--text)}
.abs{position:absolute}
.nav-ribbon{left:44px;top:78px;width:842px;height:56px}
.brand-tab{left:328px;top:0;width:275px;height:110px}
.brand-name{left:328px;top:44px;width:275px;text-align:center;font-family:'Oswald',sans-serif;font-weight:500;font-size:30px;color:var(--charcoal);letter-spacing:.5px}
.brand-mark{left:452px;top:8px;width:28px;height:28px;border-radius:50%;background:var(--green)}
.main-nav a,.foot-nav a{position:absolute;font-family:'Oswald',sans-serif;color:var(--white);text-decoration:none;white-space:nowrap}
.main-nav a{top:89px;font-size:16px}
.hero{left:67px;top:125px;width:795px;height:243px;background:linear-gradient(135deg,#4f8a2c,#7fb24a 40%,#a8c27c 70%,#5e9233)}
.hero-caption{left:109px;top:237px;width:274px;height:85px;background:rgba(230,240,220,.72);border-radius:3px;font-family:'Oswald',sans-serif;color:var(--green);font-size:26px;line-height:31px;text-align:center;padding-top:10px}
.hero-arrow{top:224px;width:20px;height:40px}
.dots span{position:absolute;top:345px;width:14px;height:14px;border-radius:50%;border:2px solid var(--white);background:rgba(255,255,255,.45)}
.panel{left:67px;top:368px;width:795px;height:509px;background:var(--panel)}
.welcome h1{position:absolute;left:78px;top:377px;font-family:'PT Serif',serif;font-weight:400;font-size:19px;color:#333}
.welcome h1 span{color:var(--green)}
.welcome p{position:absolute;left:78px;width:525px;font-size:10px;line-height:13.8px;color:#555}
.signup{left:610px;top:375px;width:245px;height:205px;background:var(--green-light);border:2px solid #1ebd5a;border-radius:4px;text-align:center;font-family:'PT Serif',serif;color:var(--white)}
.signup h2{font-weight:400;font-size:19px;line-height:21px;margin-top:3px}
.field{position:absolute;left:14px;width:220px;height:24px;background:var(--white);color:#999;font-size:12px;text-align:left;padding:4px 6px}
.join{position:absolute;left:83px;top:128px;width:65px;height:24px;background:#f1f1f1;color:var(--green);font-size:15px;line-height:24px}
.signup-links{position:absolute;left:0;top:162px;width:100%;font-size:11.5px}
.rule{left:83px;top:597px;width:763px;height:2px;background:var(--white);border-top:1px solid #ddd}
.services-title{left:67px;top:606px;width:795px;text-align:center;font-family:'PT Serif',serif;font-size:18px;color:var(--green)}
.card{top:634px;height:219px;width:240px;border:3px solid;border-radius:9px;background:var(--white)}
.plans{left:82px;border-color:var(--charcoal)}
.plan{position:absolute;left:18px;font-family:'PT Serif',serif;font-size:16px;color:#333}
.buy{position:absolute;left:152px;width:73px;height:24px;color:var(--white);font-family:'PT Serif',serif;font-size:15px;line-height:24px;padding-left:32px}
.buy svg{position:absolute;left:12px;top:5px}
.feature h3{font-family:'PT Serif',serif;font-weight:400;font-size:17px;text-align:center;margin-top:6px}
.feature .photo{position:absolute;left:12px;top:32px;width:216px;height:81px}
.feature p{position:absolute;left:13px;top:119px;width:216px;font-size:10px;line-height:13.8px;color:#777;letter-spacing:.2px}
.security{left:348px;border-color:var(--green)}
.security h3{color:var(--green)}
.access{left:608px;border-color:var(--orange)}
.access h3{color:var(--orange)}
.news-band{left:67px;top:877px;width:795px;height:202px;background:var(--green);color:var(--white)}
.band-title{position:absolute;font-family:'PT Serif',serif;font-size:18px;font-weight:400}
.news-item{position:absolute;left:16px;width:392px;border-bottom:1px solid #d7e8dc;font-size:9.6px;line-height:13.8px;padding-bottom:3px}
.news-item .date{color:#0c2a16;font-size:9px}
.follow{position:absolute;left:621px;top:28px;width:164px;height:20px;background:#f4f4f4;border:1px solid #ccc;border-radius:3px;color:#222;font-size:10px;line-height:18px;padding-left:27px}
.follow i{position:absolute;left:7px;top:4px;width:11px;height:11px;border-radius:50%;background:#3aa0dd}
.tweet{position:absolute;left:430px;width:358px;height:66px;font-size:9.2px;line-height:13.8px}
.tweet .avatar{position:absolute;left:0;top:0;width:52px;height:52px;background:linear-gradient(#c9b39a,#8a6a4e)}
.tweet .body{position:absolute;left:60px;top:-2px;width:296px}
.tweet b{font-size:11px}
.tweet .more{color:#0c2a16}
.footer{left:67px;top:1104px;width:795px;height:88px;background:var(--orange)}
.foot-nav a{top:21px;font-size:14px}
.social{position:absolute;top:7px;width:40px;height:40px;border-radius:50%;border:2px solid var(--green);background:var(--charcoal)}
.social.g{background:var(--green);border-color:#0ea34b}
.copyright{position:absolute;left:0;top:68px;width:100%;text-align:center;font-size:10px;color:var(--white)}
.copyright b{text-decoration:underline}
</style>
</head>
<body>

<svg class="abs nav-ribbon" viewBox="0 0 842 56" aria-hidden="true">
  <polygon points="0,8 16,8 16,56 0,56 6,32" fill="var(--green)"/>
  <polygon points="842,8 826,8 826,56 842,56 836,32" fill="var(--green)"/>
  <rect x="16" y="0" width="810" height="54" fill="var(--green)"/>
  <polygon points="16,54 24,56 24,54" fill="var(--green-dark)"/>
</svg>
<svg class="abs brand-tab" viewBox="0 0 275 110" aria-hidden="true">
  <polygon points="0,0 275,0 275,78 137,110 0,78" fill="#ececec"/>
</svg>
<div class="abs brand-mark"></div>
<div class="abs brand-name">VERDANT LODGE 17</div>

<nav class="main-nav">
  <a style="left:95px">HOME</a>
  <a style="left:163px">ABOUT</a>
  <a style="left:246px">SERVICES</a>
  <a style="left:577px">Blog</a>
  <a style="left:645px">TESTIMONIAL</a>
  <a style="left:758px">CONTACT US</a>
</nav>

<div class="abs hero" role="img" aria-label="Close-up photo of green cannabis leaves"></div>
<div class="abs hero-caption">Supporting the care &amp;<br>cultivation of cannabis</div>
<svg class="abs hero-arrow" style="left:83px" viewBox="0 0 20 40" aria-hidden="true"><polyline points="16,2 3,20 16,38" fill="none" stroke="#fff" stroke-width="2"/></svg>
<svg class="abs hero-arrow" style="left:829px" viewBox="0 0 20 40" aria-hidden="true"><polyline points="4,2 17,20 4,38" fill="none" stroke="#fff" stroke-width="2"/></svg>
<div class="dots">
  <span style="left:421px;background:#555"></span>
  <span style="left:445px"></span>
  <span style="left:470px"></span>
  <span style="left:494px"></span>
</div>

<div class="abs panel"></div>
<section class="welcome">
  <h1>Welcome to <span>VERDANT LODGE 17</span></h1>
  <p style="top:403px">Lorem Ipsum is simply dummy text of the printing and typesetting industry. Lorem Ipsum has been the industry's standard dummy text ever since the 1500s, when an unknown printer took a galley of type and scrambled it to make a type specimen book. It has survived not only five centuries.</p>
  <p style="top:458px">Lorem Ipsum is simply dummy text of the printing and typesetting industry. Lorem Ipsum has been the industry's standard Lorem Ipsum is simply dummy text of the printing and typesetting industry. Lorem Ipsum has been the industry's standard dummy text ever since the 1500s, when an unknown printer took a galley of type and scrambled it to make a type specimen book. It has survived not only five centuries.</p>
  <p style="top:527px">Lorem Ipsum is simply dummy text of the printing and typesetting industry. Lorem Ipsum has been the industry's standard dummy text ever since the 1500s, when an unknown printer took a galley of type and scrambled it to make a type specimen book. It has survived not only five centuries.</p>
</section>

<aside class="abs signup">
  <h2>A Better Way<br>To Do Business</h2>
  <div class="field" style="top:55px">Enter your name</div>
  <div class="field" style="top:96px">Enter your Email</div>
  <div class="join">JOIN</div>
  <div class="signup-links">Login &nbsp;|&nbsp; Forget Password</div>
</aside>

<div class="abs rule"></div>
<h2 class="abs services-title" style="font-weight:400">SERVICES</h2>

<section class="abs card plans">
  <div class="plan" style="top:22px">Bronze Plan</div>
  <div class="buy" style="top:22px;background:var(--charcoal)"><svg width="16" height="14" viewBox="0 0 16 14"><path d="M0 1h3l2 8h9l2-6H5" fill="none" stroke="#fff" stroke-width="2"/><circle cx="6" cy="12" r="1.5" fill="#fff"/><circle cx="13" cy="12" r="1.5" fill="#fff"/></svg>BUY</div>
  <div class="plan" style="top:85px">Silver Plan</div>
  <div class="buy" style="top:85px;background:var(--green)"><svg width="16" height="14" viewBox="0 0 16 14"><path d="M0 1h3l2 8h9l2-6H5" fill="none" stroke="#fff" stroke-width="2"/><circle cx="6" cy="12" r="1.5" fill="#fff"/><circle cx="13" cy="12" r="1.5" fill="#fff"/></svg>BUY</div>
  <div class="plan" style="top:157px">Platinum Plan</div>
  <div class="buy" style="top:157px;background:var(--orange)"><svg width="16" height="14" viewBox="0 0 16 14"><path d="M0 1h3l2 8h9l2-6H5" fill="none" stroke="#fff" stroke-width="2"/><circle cx="6" cy="12" r="1.5" fill="#fff"/><circle cx="13" cy="12" r="1.5" fill="#fff"/></svg>BUY</div>
</section>

<section class="abs card feature security">
  <h3>Security</h3>
  <div class="photo" role="img" aria-label="Photo of two security cameras" style="background:linear-gradient(#f2f2f2,#cfcfcf)"></div>
  <p>Lorem Ipsum is simply dummy text of the printing and typesetting industry. Lorem Ipsum has been the industry's standard dummy text Lorem Ipsum is simply ever since the 1500s.</p>
</section>

<section class="abs card feature access">
  <h3>Online Access</h3>
  <div class="photo" role="img" aria-label="Photo of monitors showing plants being tended" style="background:linear-gradient(90deg,#dcdcdc,#6e8a55 35%,#3b4a33 60%,#dcdcdc)"></div>
  <p>Lorem Ipsum is simply dummy text of the printing and typesetting industry. Lorem Ipsum has been the industry's standard dummy text Lorem Ipsum is simply ever since the 1500s.</p>
</section>

<section class="abs news-band">
  <h2 class="band-title" style="left:19px;top:10px">Latest News</h2>
  <div class="news-item" style="top:46px;left:16px"><div class="date">Dec 17 2014</div>Lorem Ipsum is simply dummy text of the printing and typesetting industry. Lorem Ipsum has been the industry's standard dummy text ever since the 1500s.</div>
  <div class="news-item" style="top:94px"><div class="date">Dec 14 2014</div>Lorem Ipsum is simply dummy text of the printing and typesetting industry. Lorem Ipsum has been the industry's standard dummy text ever since the 1500s.</div>
  <div class="news-item" style="top:143px"><div class="date">Dec 10 2014</div>Lorem Ipsum is simply dummy text of the printing and typesetting industry.</div>

  <h2 class="band-title" style="left:428px;top:10px">Tweets</h2>
  <div style="position:absolute;left:430px;top:31px;font-size:12px">Tweets</div>
  <div class="follow"><i></i>Follow @VERDANT LODGE 17</div>
  <div class="tweet" style="top:65px;border-bottom:1px solid #d7e8dc">
    <div class="avatar" role="img" aria-label="Profile photo"></div>
    <div class="body"><b>Leafwise</b> @ Leafwise<br>Lorem Ipsum is simply dummy @ dummy text of the printing and typesetting industry. Lorem Ipsum has been the industry's standard<br><span class="more">Expand</span></div>
  </div>
  <div class="tweet" style="top:135px">
    <div class="avatar" role="img" aria-label="Profile photo"></div>
    <div class="body"><b>Leafwise</b> @ Leafwise<br>Lorem Ipsum is simply dummy @ dummy text of the printing and typesetting industry. Lorem Ipsum has been.<br><span class="more">Expand</span></div>
  </div>
</section>

<footer class="abs footer">
  <nav class="foot-nav">
    <a style="left:28px;color:#111">HOME</a>
    <a style="left:93px">ABOUT</a>
    <a style="left:162px">SERVICES</a>
    <a style="left:246px">Blog</a>
    <a style="left:305px">TESTIMONIAL</a>
    <a style="left:404px">CONTACT US</a>
  </nav>
  <div class="social" style="left:626px" aria-label="Social link"></div>
  <div class="social g" style="left:682px" aria-label="Social link"></div>
  <div class="social g" style="left:739px" aria-label="Social link"></div>
  <div class="copyright">© <b>VERDANT LODGE 17</b> - 2014. All Rights Reserved.</div>
</footer>

</body>
</html>
```